Cleaning and Maintenance Business card design

i provide a service which includes;
Professional Window Cleaning
Lawn Mowing
Gardening
Painting
Rubbish Removal
Commercial Cleaning
Property & Ground Maintenance
Pensioner discounts apply
Call now for an inquiry and free quote
`Double sided` (willing to pay any extra)
i would like a design that is not too crowded and straight to the point.
i want the reader to know exactly what the business is about from one glance.
i would like the logo to communicate the businesses 3 main aspects (window cleaning, lawn mowing, and Cleaning)
Thanks.
Industry/Entity Type
Business
Contact Information for Business Card
Business name : Brick 4 Bloom*
* with subline 'And Everything In Between' (smaller font)
Name: Tom Vasharoukis
Mobile: 0417 952 164
Email: t.vasharoukis@pebblemail.net
ABN: 37 514 209 861
`Double Sided`
Logo Text
Brick 4 Bloom
Logo styles of interest
Character Logo
Look and feel

```html
<!DOCTYPE html>
<html lang="en">
<head>
<meta charset="utf-8">
<title>Brick 4 Bloom – Business Card</title>
<link href="https://fonts.googleapis.com/css2?family=Arvo:ital,wght@0,700;1,400&family=Arimo:wght@400;700&display=swap" rel="stylesheet">
<style>
  :root {
    --green-light: #9cf50a;
    --green-mid: #7fe000;
    --green-deep: #4fae00;
    --ink-white: #ffffff;
    --ink-dark: #2e3a1c;
  }
  html, body {
    margin: 0;
    padding: 0;
    width: 1200px;
    height: 693px;
    overflow: hidden;
    background: #ffffff;
  }
  .card {
    position: relative;
    width: 1200px;
    height: 693px;
    overflow: hidden;
    background: radial-gradient(ellipse 75% 70% at 50% 50%, var(--green-light) 0%, var(--green-mid) 55%, var(--green-deep) 100%);
    font-family: "Arimo", Arial, sans-serif;
    color: var(--ink-white);
  }
  .brand-name {
    position: absolute;
    left: 0;
    right: 0;
    top: 150px;
    margin: 0;
    text-align: center;
    font-family: "Arvo", Georgia, serif;
    font-weight: 700;
    font-size: 128px;
    line-height: 1;
    letter-spacing: 1px;
    color: var(--ink-white);
  }
  .tagline {
    position: absolute;
    left: 566px;
    top: 330px;
    margin: 0;
    font-family: "Arvo", Georgia, serif;
    font-style: italic;
    font-weight: 400;
    font-size: 31px;
    color: var(--ink-dark);
    white-space: nowrap;
  }
  .services {
    position: absolute;
    left: 0;
    right: 0;
    top: 438px;
    margin: 0;
    padding: 0;
    list-style: none;
    text-align: center;
    font-size: 23.5px;
    line-height: 34px;
  }
  .services li { display: inline; margin: 0 4px; }
  .services .break { display: block; height: 0; }
  .call {
    position: absolute;
    left: 155px;
    top: 557px;
    display: flex;
    align-items: center;
    gap: 22px;
  }
  .call-icon { width: 50px; height: 84px; display: block; }
  .call-text {
    margin: 0;
    font-size: 39px;
    font-weight: 400;
    white-space: nowrap;
  }
  .call-text strong { font-weight: 700; }
</style>
</head>
<body>
  <main class="card">
    <h1 class="brand-name">Brick 4 Bloom</h1>
    <p class="tagline">And Everything In Between ...</p>

    <ul class="services">
      <li>*Professional Window Cleaning</li>
      <li>*Lawn Mowing</li>
      <li>*Gardening</li>
      <li>*Painting</li>
      <li class="break"></li>
      <li>*Rubbish Removal</li>
      <li>*Commercial Cleaning</li>
      <li>*Property &amp; Ground Maintenance</li>
    </ul>

    <div class="call">
      <svg class="call-icon" viewBox="0 0 50 84" aria-hidden="true">
        <rect x="2" y="2" width="46" height="80" rx="7" fill="none" stroke="#ffffff" stroke-width="4"/>
        <rect x="8" y="12" width="34" height="52" fill="#ffffff"/>
        <circle cx="25" cy="73" r="3.5" fill="#ffffff"/>
      </svg>
      <p class="call-text"><strong>CALL NOW</strong> for an inquiry &amp; <strong>FREE</strong> quote</p>
    </div>
  </main>
</body>
</html>
```